EverLeafGoods - Stationery, logo provided
Business card, headed paper, comp slip, envelope and A4 folded literature doc wallet
EverLeafGoods - Stationery, logo provided -
Creative Brief
Professional
Mark du Verrand
Les Boulins Rue du Cotil St. Andrews Guernsey GY5 8QT
mark@everleafg.co
www.everleafg.co
The headed paper footer should include the words "Kestrow Limited trading as EverLeafGoods" and possibly on the next line, "Registered in Guernsey - Company No. 71624"
Can be blank or leave to your creativity...

```html
<!DOCTYPE html>
<html lang="en">
<head>
<meta charset="utf-8">
<title>EverLeafGoods – Business Cards</title>
<link href="https://fonts.googleapis.com/css2?family=Nunito:wght@400;600;800&display=swap" rel="stylesheet">
<style>
  :root{
    --bg:#ecebe8;
    --blue-deep:#1346a8;
    --blue:#1e6fd0;
    --blue-light:#3fa0ea;
    --green:#6cbf2a;
    --green-dark:#3f9a1f;
    --white:#ffffff;
    --ink:#4a4a4a;
    --ink-soft:#6b6b6b;
  }
  *{margin:0;padding:0;box-sizing:border-box}
  html,body{width:1200px;height:799px;overflow:hidden}
  body{background:var(--bg);font-family:'Nunito',sans-serif;position:relative}
  .card{position:absolute;width:408px;height:264px;border-radius:26px;overflow:hidden;
        box-shadow:0 4px 14px rgba(0,0,0,.18)}
  .card svg.card-bg{position:absolute;inset:0;width:100%;height:100%}
  .card--contact{left:72px;top:96px}
  .card--brand{left:624px;top:98px}
  .card--back{left:356px;top:430px}

  .brand{position:absolute;display:flex;align-items:center;gap:10px}
  .brand__dot{width:70px;height:70px;border-radius:50%;background:var(--green)}
  .brand__name{font-weight:800;font-size:27px;color:var(--blue-deep);letter-spacing:-.3px}
  .card--contact .brand{left:36px;top:60px}
  .card--brand .brand{left:42px;top:64px}
  .card--back .brand{left:170px;top:82px}

  .holder{position:absolute;right:26px;top:26px;font-weight:800;font-size:14px;color:var(--green-dark)}
  .phones{position:absolute;right:22px;top:138px;list-style:none;font-size:11px;color:var(--ink);line-height:16px;text-align:right}
  .phones li{display:flex;justify-content:flex-end;align-items:center;gap:5px}
  .phones svg{width:10px;height:10px}
  .address{position:absolute;left:40px;top:176px;font-size:11px;line-height:16px;color:var(--ink-soft);width:150px}
  .web{position:absolute;font-size:11px;font-weight:800;color:var(--ink)}
  .web span{color:var(--green-dark)}
  .card--contact .web{right:24px;top:204px}
  .card--brand .web{right:52px;top:206px}
  .card--back .web{left:0;right:0;top:178px;text-align:center;color:var(--white)}
  .card--back .web span{color:var(--white)}
</style>
</head>
<body>

<section class="card card--contact" aria-label="Business card front with contact details">
  <svg class="card-bg" viewBox="0 0 408 264" preserveAspectRatio="none" aria-hidden="true">
    <defs>
      <linearGradient id="blueA" x1="0" y1="0" x2="1" y2="1">
        <stop offset="0" stop-color="#3fa0ea"/><stop offset="1" stop-color="#1346a8"/>
      </linearGradient>
      <linearGradient id="greenA" x1="0" y1="0" x2="1" y2="1">
        <stop offset="0" stop-color="#8bd23a"/><stop offset="1" stop-color="#3f9a1f"/>
      </linearGradient>
    </defs>
    <rect width="408" height="264" fill="url(#blueA)"/>
    <ellipse cx="250" cy="250" rx="280" ry="130" fill="url(#greenA)"/>
    <ellipse cx="215" cy="118" rx="270" ry="135" fill="#fff"/>
  </svg>
  <p class="holder">Mark du Verrand</p>
  <div class="brand"><span class="brand__dot"></span><span class="brand__name">EverLeafGoods</span></div>
  <ul class="phones">
    <li>0044 1481 503927
      <svg viewBox="0 0 10 10"><path d="M2 1l2 2-1 1.5a5 5 0 0 0 2.5 2.5L7 6l2 2-1.5 1.5C4 9 1 6 .5 2.5z" fill="#4a4a4a"/></svg></li>
    <li>0044 7781 628415
      <svg viewBox="0 0 10 10"><rect x="2.5" y=".5" width="5" height="9" rx="1" fill="#4a4a4a"/></svg></li>
    <li>0044 1481 376052
      <svg viewBox="0 0 10 10"><rect x="1" y="3" width="8" height="5" rx="1" fill="#4a4a4a"/><rect x="3" y="1" width="4" height="2" fill="#4a4a4a"/></svg></li>
    <li>mark@everleafg.co
      <svg viewBox="0 0 10 10"><rect x=".5" y="2" width="9" height="6" fill="none" stroke="#4a4a4a"/><path d="M.5 2L5 5.5 9.5 2" fill="none" stroke="#4a4a4a"/></svg></li>
  </ul>
  <p class="address">Les Boulins Rue du Cotil St. Andrews Guernsey GY5 8QT</p>
  <p class="web">www.<span>everleafg</span>.co</p>
</section>

<section class="card card--brand" aria-label="Business card front with brand">
  <svg class="card-bg" viewBox="0 0 408 264" preserveAspectRatio="none" aria-hidden="true">
    <defs>
      <linearGradient id="blueB" x1="0" y1="0" x2="1" y2="1">
        <stop offset="0" stop-color="#3fa0ea"/><stop offset="1" stop-color="#1346a8"/>
      </linearGradient>
      <linearGradient id="greenB" x1="0" y1="0" x2="1" y2="1">
        <stop offset="0" stop-color="#8bd23a"/><stop offset="1" stop-color="#3f9a1f"/>
      </linearGradient>
    </defs>
    <rect width="408" height="264" fill="url(#blueB)"/>
    <ellipse cx="250" cy="240" rx="270" ry="120" fill="url(#greenB)"/>
    <ellipse cx="190" cy="132" rx="240" ry="118" fill="#fff"/>
  </svg>
  <div class="brand"><span class="brand__dot"></span><span class="brand__name">EverLeafGoods</span></div>
  <p class="web">www.<span>everleafg</span>.co</p>
</section>

<section class="card card--back" aria-label="Business card back">
  <svg class="card-bg" viewBox="0 0 408 264" preserveAspectRatio="none" aria-hidden="true">
    <defs>
      <radialGradient id="blueC" cx=".45" cy=".4" r=".75">
        <stop offset="0" stop-color="#3fa0ea"/><stop offset=".6" stop-color="#1e6fd0"/><stop offset="1" stop-color="#1346a8"/>
      </radialGradient>
    </defs>
    <rect width="408" height="264" fill="url(#blueC)"/>
  </svg>
  <div class="brand"><span class="brand__dot"></span></div>
  <p class="web">www.<span>everleafg</span>.co</p>
</section>

</body>
</html>
```